Business card for Harbor Crafters
Looking for creativity
Professional
Dominic Farrow
Owner Operator
47 S Pell Avenue
Brinewick, MA 19842
@domfarrow
craftharborco@mailvane.com
www.craftharborco.com
Looking for a creative business card for my company. I have a logo and like the feel of it. The business card should have a contemporary feel and be interesting.
The name of the company and the website

```html
<!DOCTYPE html>
<html lang="en">
<head>
<meta charset="utf-8">
<title>Harbor Crafters Stationery</title>
<link href="https://fonts.googleapis.com/css2?family=Lato:wght@400;700&display=swap" rel="stylesheet">
<style>
:root{
  --brand:#1f5fae;
  --ink:#555b63;
  --rule:#9aa0a8;
  --paper:#ffffff;
  --ground:#ffffff;
  --ghost:#e6e9ee;
  --flap:#c9cdd3;
}
*{box-sizing:border-box;margin:0;padding:0}
html,body{width:1200px;height:482px;overflow:hidden;background:var(--ground)}
body{position:relative;font-family:"Lato",Arial,sans-serif;color:var(--ink)}
.sheet{position:absolute;background:var(--paper);box-shadow:0 2px 8px rgba(0,0,0,.28)}
.brand-name{font-family:"Lato",Arial,sans-serif;font-weight:700;color:var(--brand);letter-spacing:1px;line-height:1;white-space:nowrap}
.side-band{position:absolute;left:0;width:6px;bottom:0;background:var(--brand)}
.ghost-name{position:absolute;font-weight:700;color:var(--ghost);letter-spacing:1px;line-height:1}
.small-lines{position:absolute;font-size:6px;line-height:8.5px;color:var(--ink);white-space:nowrap}

/* fax sheet */
.fax{left:41px;top:34px;width:314px;height:417px}
.fax .side-band{top:62px}
.fax .brand-name{position:absolute;left:20px;top:20px;font-size:24px}
.fax .small-lines{left:20px;top:76px}
.fax-form{position:absolute;left:20px;top:146px;width:274px;display:grid;grid-template-columns:1fr 1fr;column-gap:20px;row-gap:11px}
.field{display:flex;align-items:flex-end;font-size:6.5px}
.field span{width:30px}
.field i{flex:1;border-bottom:1px solid var(--rule);height:8px}
.checks{position:absolute;left:20px;top:224px;display:flex;gap:10px;font-size:6px;white-space:nowrap}
.checks span{display:flex;align-items:center;gap:3px}
.checks b{width:6px;height:6px;border:1px solid var(--rule);border-radius:50%}
.fax .ghost-name{right:16px;bottom:20px;font-size:28px}

/* envelopes */
.env-front{left:398px;top:52px;width:236px;height:158px}
.env-front .brand-name{position:absolute;left:18px;top:20px;font-size:20px}
.env-front .stripe{position:absolute;left:18px;top:47px;width:170px;height:2px;background:var(--brand)}
.env-front .small-lines{left:20px;top:51px;font-size:5px}
.env-back{left:398px;top:258px;width:236px;height:168px}
.env-back svg{position:absolute;inset:0}
.env-back .brand-name{position:absolute;left:0;right:0;top:28px;text-align:center;font-size:18px}

/* letterhead */
.letter{left:799px;top:34px;width:308px;height:417px}
.letter .side-band{top:62px}
.letter .brand-name{position:absolute;left:20px;top:20px;font-size:24px}
.letter .small-lines{left:20px;top:76px}
.letter .ghost-name{right:16px;bottom:20px;font-size:28px}

/* business cards */
.card{position:absolute;box-shadow:0 2px 6px rgba(0,0,0,.3)}
.card-front{left:1036px;top:104px;width:76px;height:52px;background:var(--paper)}
.card-front .brand-name{position:absolute;left:6px;top:6px;font-size:8px}
.card-front .person{position:absolute;left:6px;top:19px;font-size:3.6px;line-height:5px;white-space:nowrap}
.card-front .person strong{font-size:4.4px;color:var(--brand)}
.card-back{left:1034px;top:194px;width:108px;height:66px;background:var(--brand)}
.card-back .brand-name{position:absolute;left:0;right:0;top:24px;text-align:center;font-size:10px;color:#fff}
.card-back .web{position:absolute;left:0;right:0;top:37px;text-align:center;font-size:4.5px;color:#fff}
</style>
</head>
<body>

<section class="sheet fax">
  <div class="brand-name">HARBOR</div>
  <div class="small-lines">47 S Pell Avenue<br>Brinewick, MA 19842<br>craftharborco@mailvane.com<br>www.craftharborco.com</div>
  <div class="fax-form">
    <div class="field"><span>To:</span><i></i></div>
    <div class="field"><span>From:</span><i></i></div>
    <div class="field"><span>Fax:</span><i></i></div>
    <div class="field"><span>Pages:</span><i></i></div>
    <div class="field"><span>Phone:</span><i></i></div>
    <div class="field"><span>Date:</span><i></i></div>
    <div class="field"><span>Re:</span><i></i></div>
    <div class="field"><span>CC:</span><i></i></div>
  </div>
  <div class="checks">
    <span><b></b>Urgent</span><span><b></b>For Review</span><span><b></b>Please Comment</span><span><b></b>Please Reply</span><span><b></b>Please Recycle</span>
  </div>
  <div class="ghost-name">HARBOR</div>
  <div class="side-band"></div>
</section>

<section class="sheet env-front">
  <div class="brand-name">HARBOR</div>
  <div class="stripe"></div>
  <div class="small-lines">47 S Pell Avenue, Brinewick, MA 19842</div>
</section>

<section class="sheet env-back">
  <svg width="236" height="168" viewBox="0 0 236 168" aria-hidden="true">
    <polyline points="0,0 118,78 236,0" fill="none" stroke="var(--flap)" stroke-width="1"/>
  </svg>
  <div class="brand-name">HARBOR</div>
</section>

<section class="sheet letter">
  <div class="brand-name">HARBOR</div>
  <div class="small-lines">47 S Pell Avenue<br>Brinewick, MA 19842<br>craftharborco@mailvane.com<br>www.craftharborco.com</div>
  <div class="ghost-name">HARBOR</div>
  <div class="side-band"></div>
</section>

<section class="card card-front">
  <div class="brand-name">HARBOR</div>
  <div class="person"><strong>Dominic Farrow</strong><br>Owner Operator<br>47 S Pell Avenue<br>Brinewick, MA 19842<br>craftharborco@mailvane.com</div>
</section>

<section class="card card-back">
  <div class="brand-name">HARBOR</div>
  <div class="web">www.craftharborco.com</div>
</section>

</body>
</html>
```